I am writing a book called "SMILING OPENS EVERY DOOR "

I NEED A BOOK COVER FOR MY BOOK" SMILING OPENS EVERY DOOR"
so what was the question? " ( this in smaller font)

"Smiling Opens Every Door " will need to designed to eventually be a logo , banner and business card
COLOURS MAINLY ORANGE AND WHITE (with accents bright colour )

THE BOOK IS MY LAUGHTER JOURNEY AS A PERFORMER AND ADVENTURE INDIA LEARNING ABOUT LAUGHTER YOGA WHICH I WILL BE TEACHING

I do not want photos on the front cover ..
The look could be modern and eye-catching
I have also just been to India to learn Laughing Yoga with Dr Tobin Verhaal

Thank-you so much everyone for your brilliant designs . i am overwhelmed with your talent . i hope to work with you all again soon ! Marnie  

Target Market(s)

"Adults based in western speaking countries aged 25 to 60 that want to learn to laugh more
Also this book will be sold at my conference workshops

Industry/Entity Type

Business

Requirements
Must have
• ORANGE AND WHITE
CAN HAVE AQUA , HOT PINK , LIME GREEN, YELLOW ACCENTS

THESE WILL BE DIFFERENT AREAS WILL COVERING IN MY BOOK
EG LAUGHTER NAD BREAT CANCER ( PINK)
LAUGHTER NAD DEPRESSION ( BLUE)
LAUGHTER AND KIDS ( YELLOW)

NO Photos on front cover
Should not have
• No photos

```html
<!DOCTYPE html>
<html lang="en">
<head>
<meta charset="utf-8">
<title>Smiling Opens Every Door — Book Cover</title>
<link rel="stylesheet" href="https://fonts.googleapis.com/css2?family=Cinzel:wght@700&family=Cormorant+Garamond:ital,wght@0,500;1,500&display=swap">
<style>
  :root {
    --backdrop: #4d4a4a;
    --paper: #ffffff;
    --title-orange: #e8892a;
    --byline-grey: #4a4a4a;
    --art-yellow: #fff200;
    --art-amber: #f4b200;
    --art-orange: #ee9a12;
  }
  html, body {
    margin: 0;
    padding: 0;
    width: 1200px;
    height: 1000px;
    overflow: hidden;
    background: var(--backdrop);
  }
  .canvas {
    position: relative;
    width: 1200px;
    height: 1000px;
  }
  .cover {
    position: absolute;
    left: 231px;
    top: 20px;
    width: 739px;
    height: 957px;
    background: var(--paper);
    overflow: hidden;
  }
  .cover-art {
    position: absolute;
    left: 0;
    top: 0;
    width: 739px;
    height: 957px;
  }
  .title-block {
    position: absolute;
    right: 180px;
    top: 413px;
    text-align: right;
  }
  .book-title {
    margin: 0;
    font-family: "Cinzel", "Trajan Pro", serif;
    font-weight: 700;
    font-size: 22px;
    letter-spacing: 0.2px;
    line-height: 26px;
    color: var(--title-orange);
    white-space: nowrap;
  }
  .byline {
    margin: 0;
    font-family: "Cormorant Garamond", Georgia, serif;
    font-weight: 500;
    font-size: 18px;
    line-height: 22px;
    color: var(--byline-grey);
    white-space: nowrap;
  }
  .byline em {
    font-style: italic;
    margin-right: 3px;
  }
  .subtitle {
    margin: 2px 0 0;
    font-family: "Cormorant Garamond", Georgia, serif;
    font-style: italic;
    font-weight: 500;
    font-size: 14px;
    line-height: 18px;
    color: var(--title-orange);
    white-space: nowrap;
  }
</style>
</head>
<body>
<div class="canvas">
  <main class="cover">
    <svg class="cover-art" viewBox="231 20 739 957" role="img" aria-label="Sunburst arc illustration in yellow and orange tones">
      <defs>
        <linearGradient id="sun-glow" gradientUnits="userSpaceOnUse" x1="970" y1="540" x2="231" y2="977">
          <stop offset="0" stop-color="var(--art-yellow)"/>
          <stop offset="0.6" stop-color="var(--art-amber)"/>
          <stop offset="1" stop-color="var(--art-orange)"/>
        </linearGradient>
      </defs>
      <path class="sun-area" fill="url(#sun-glow)" d="M994,540 A489 489 0 0 1 16,540 Z"/>
    </svg>
    <header class="title-block">
      <h1 class="book-title">“SMILING OPENS EVERY DOOR”</h1>
      <p class="byline"><em>by</em> Marnie Brightwell</p>
      <p class="subtitle">so what was the question?</p>
    </header>
  </main>
</div>
</body>
</html>
```